Book Cover Design | Science & Nature

We are looking for a cover design for our new educational book titled "Moths Beyond the Hedge".
The full title on the cover can either only be "Moths Beyond the Hedge" or "Garden Moths Beyond the Hedge - a pocket handbook". Up to you what looks good. If the latter, the words "Moths Beyond the Hedge" should be written in larger letters.
The book has a lot information about spiders in general and provides a convenient and understandable identification guide about spiders in California.
The target audience are normal, non-scientist readers who would like to get a simple guide that helps them identify common spiders they will find inside their homes and gardens.
The book is written in an understandable, non-scientific language and contains numerous illustrations and identification sheets of all common spiders.
We are fairly open to suggestions about the design. It should not be too plain as it is not a classic boring science book, but aimed at the average reader. Readers are both male and female, aged 30 and above.
If you know nothing about spiders but would like to know what the spiders in your backyard are, which ones are dangerous and if you want to learn more about spiders, this should be the book you will want to buy!
The author is Dale Prowse. In addition to the author, the book cover should show "Brindlewing.com" - The author can be at the bottom and the website on the top or vice versa.
The cover size is 6" x 9" (15.24 x 22.86 cm). The book has around 150 pages. The back of the book should have a placeholder for the barcode as well as some text. It should also have a quick overview of the main benefits of the book: Easily understandable for non-scientist readers, helpful illustrations, tips on how to deal with spiders in the house and with spider bites. We will obviously add the text later.
I've attached a few of the illustrations as I think they could be used to already give the reader a feeling what they will get with the book. If you think a stock photo will work better than the illustrations, that is fine too.

Target Market(s)

Average readers in the United States wanting to learn more about spiders

Industry/Entity Type

Science, Nature, Spiders, Animals, Education

Requirements
Must have
• When the artwork is generated, the files we would like to receive are: The original working file PSD (Photoshop Document - so any text and images can be edited) All the working elements including: illustrations, photos, graphics and fonts A high resolution (300 dpi), 8.5 x 11 (o- Once r larger) file A JPG file in the exact size specifications and color required by our publisher A JPG file in the exact size for online POD or ebook (Pagelume requires 900x600 ) A JPG black and white (gray scale) variation
Nice to have
• A text (overlay?) could point out some of the advantages of this book: Illustrations and identification guides for all common California spiders, tips on how to get rid of spiders from inside the house, tips on how to deal with arachnophobia, etc. This is optional. Maybe something like "An easy to understand identification guide with plenty of tips and illustrations".
Should not have
• Very dark colors or very feminine colors or shapes.

```html
<!DOCTYPE html>
<html lang="en">
<head>
<meta charset="utf-8">
<title>Moths Beyond the Hedge – Cover Spread</title>
<link href="https://fonts.googleapis.com/css2?family=Oswald:wght@200;500;700&family=Roboto+Condensed:wght@700&display=swap" rel="stylesheet">
<style>
  :root {
    --page-bg: #ffffff;
    --paper: #f1f1f0;
    --paper-shade: #dcdcdb;
    --tear-line: #b9bab9;
    --ink: #111111;
    --accent-red: #ee1c1c;
    --barcode-box: #ffffff;
    --spider-yellow: #e4dc3a;
    --spider-gold: #c9a43f;
    --spider-red: #9c4128;
    --spider-black: #262626;
    --spider-green: #79a43c;
    --spider-brown: #8c6c4d;
    --spider-rust: #a85a32;
  }
  * { margin: 0; padding: 0; box-sizing: border-box; }
  html, body {
    width: 882px; height: 1200px; overflow: hidden;
    background: var(--page-bg);
  }
  .spread {
    position: absolute; left: 10px; top: 299px;
    width: 862px; height: 602px;
    background: var(--paper);
    overflow: hidden;
    box-shadow: 0 0 0 1px #e2e2e2;
  }
  .paper-texture, .artwork { position: absolute; inset: 0; width: 862px; height: 602px; }
  .illustration { stroke: rgba(0,0,0,0.12); stroke-width: 1; }
  .back-cover, .spine, .front-cover { position: absolute; top: 0; height: 602px; }
  .back-cover { left: 0; width: 416px; }
  .spine { left: 416px; width: 44px; }
  .front-cover { left: 460px; width: 402px; }

  .back-tagline {
    position: absolute; left: 0; width: 416px; top: 121px;
    text-align: center; color: var(--accent-red);
    font: 700 8px/1 "Roboto Condensed", sans-serif;
  }
  .back-copy {
    position: absolute; left: 60px; width: 288px;
    color: var(--ink); text-align: justify; text-align-last: center;
    font: 700 9.4px/13px "Roboto Condensed", sans-serif;
  }
  .back-copy.first { top: 139px; }
  .back-copy.second { top: 246px; }
  .barcode-placeholder {
    position: absolute; left: 224px; top: 487px; width: 122px; height: 51px;
    background: var(--barcode-box);
  }

  .spine-title, .spine-author {
    position: absolute; left: 22px; white-space: nowrap;
    transform: translate(-50%, -50%) rotate(-90deg);
    font-family: "Oswald", sans-serif; color: var(--ink);
  }
  .spine-title { top: 240px; font-weight: 200; font-size: 20px; }
  .spine-title .accent { color: var(--accent-red); font-weight: 500; }
  .spine-author { top: 478px; font-weight: 700; font-size: 15px; }

  .site-name {
    position: absolute; left: 148px; top: 23px;
    font: 500 15px/1 "Oswald", sans-serif; color: var(--ink);
    letter-spacing: 0.2px;
  }
  .title-main {
    position: absolute; right: 26px; top: 40px;
    font: 700 104px/1 "Oswald", sans-serif; color: var(--accent-red);
    letter-spacing: -1px;
  }
  .title-sub {
    position: absolute; right: 24px; top: 158px;
    font: 200 47px/1 "Oswald", sans-serif; color: var(--ink);
    letter-spacing: -0.5px; white-space: nowrap;
  }
  .title-kicker {
    position: absolute; left: 56px; top: 280px;
    font: 500 18px/1 "Oswald", sans-serif; color: var(--ink);
    letter-spacing: 4px; white-space: nowrap;
  }
  .author-name {
    position: absolute; left: 0; width: 402px; padding-right: 10px; top: 528px;
    text-align: center;
    font: 700 30px/1 "Oswald", sans-serif; color: var(--ink);
  }
</style>
</head>
<body>
  <section class="spread">
    <svg class="paper-texture" viewBox="0 0 862 602" role="img" aria-label="Torn paper layered background in pale greys">
      <defs>
        <linearGradient id="paperGrad" x1="0" y1="0" x2="0" y2="1">
          <stop offset="0" stop-color="#f4f4f3"/>
          <stop offset="1" stop-color="#ebebea"/>
        </linearGradient>
      </defs>
      <rect width="862" height="602" fill="url(#paperGrad)"/>
      <path d="M0 100 C150 90 300 120 460 105 S720 150 862 130 L862 175 C700 190 560 160 420 175 S150 140 0 150 Z" fill="var(--paper-shade)" opacity="0.55"/>
      <path d="M0 220 C200 210 350 250 520 235 S760 260 862 250 L862 290 C700 300 500 280 330 300 S120 270 0 280 Z" fill="var(--paper-shade)" opacity="0.45"/>
      <path d="M0 100 C150 90 300 120 460 105 S720 150 862 130" fill="none" stroke="var(--tear-line)" stroke-width="1.2"/>
      <path d="M0 220 C200 210 350 250 520 235 S760 260 862 250" fill="none" stroke="var(--tear-line)" stroke-width="1.2"/>
      <path d="M270 602 C330 520 420 470 520 430 S700 360 862 330" fill="none" stroke="var(--tear-line)" stroke-width="1"/>
    </svg>

    <svg class="artwork" viewBox="0 0 862 602">
      <ellipse class="illustration" cx="548" cy="22" rx="34" ry="22" fill="var(--spider-yellow)" role="img" aria-label="Illustration of a yellow crab spider"/>
      <ellipse class="illustration" cx="62" cy="42" rx="48" ry="30" fill="var(--spider-gold)" role="img" aria-label="Illustration of a yellow and black garden spider"/>
      <ellipse class="illustration" cx="372" cy="70" rx="34" ry="24" fill="var(--spider-red)" role="img" aria-label="Illustration of a red-backed jumping spider"/>
      <ellipse class="illustration" cx="838" cy="300" rx="22" ry="20" fill="var(--spider-black)" role="img" aria-label="Illustration of a black widow spider"/>
      <ellipse class="illustration" cx="506" cy="374" rx="30" ry="26" fill="var(--spider-green)" role="img" aria-label="Illustration of a green lynx spider"/>
      <ellipse class="illustration" cx="92" cy="520" rx="80" ry="66" fill="var(--spider-brown)" role="img" aria-label="Illustration of a wolf spider"/>
      <ellipse class="illustration" cx="486" cy="548" rx="30" ry="36" fill="var(--spider-rust)" role="img" aria-label="Illustration of a rust-coloured woodlouse spider"/>
      <ellipse class="illustration" cx="808" cy="468" rx="50" ry="44" fill="var(--spider-brown)" role="img" aria-label="Illustration of a brown widow spider"/>
    </svg>

    <div class="back-cover">
      <p class="back-tagline">An easy to understand identification guide with plenty of tips and illustrations</p>
      <p class="back-copy first">Lorem ipsum dolor sit amet, consectetur adipiscing elit. Mauris nec nisi odio. Etiam fermentum maximus justo, nec rutrum massa efficitur non. Donec ac sagittis massa. Nunc eu sapien tortor. Phasellus lacinia a tortor vitae pretium. Etiam vel purus augue. Etiam sollicitudin sagittis eros, non eleifend dui viverra eu.</p>
      <p class="back-copy second">Ut vestibulum ultrices ultrices. Ut ut vulputate eros. Praesent sed maximus neque. Suspendisse vulputate ultricies lectus sed scelerisque. Cras cursus urna vel nunc dictum tristique. Suspendisse ultricies ante massa, sit amet tempus ipsum iaculis id. Donec ac arcu lectus. Phasellus id ultricies mauris. Curabitur ac lorem neque. Vestibulum suscipit mauris est, sit amet tincidunt turpis lobortis in. Nam tincidunt ante eu turpis eleifend imperdiet. Suspendisse potenti. Proin rhoncus iaculis sapien, non finibus augue pulvinar eget. Etiam tristique leo quis mauris consectetur posuere. In ornare consectetur dignissim.</p>
      <div class="barcode-placeholder"></div>
    </div>

    <div class="spine">
      <p class="spine-title"><span class="accent">MOTHS</span> BEYOND THE HEDGE</p>
      <p class="spine-author">DALE PROWSE</p>
    </div>

    <div class="front-cover">
      <p class="site-name">BRINDLEWING.COM</p>
      <h1 class="title-main">MOTHS</h1>
      <p class="title-sub">BEYOND THE HEDGE</p>
      <p class="title-kicker">A POCKET HANDBOOK</p>
      <p class="author-name">DALE PROWSE</p>
    </div>
  </section>
</body>
</html>
```